verano habitat

I need a brochure that can help me sell memberships or enrollments into a delivery system for homes of natural products including flower arrangements and also hotel day passes . enclosed are the text and the current logo.

```html
<!DOCTYPE html>
<html lang="es">
<head>
<meta charset="utf-8">
<title>Verano Habitat — Folleto de membresía</title>
<link rel="stylesheet" href="https://fonts.googleapis.com/css2?family=Source+Sans+3:wght@400;600;700&display=swap">
<style>
  :root{
    --bg:#d4d5d7;
    --paper:#ffffff;
    --green:#5c9a2e;
    --green-light:#8cc63f;
    --green-dark:#4c8426;
    --gold:#a8952a;
    --text:#2f2f2f;
    --muted:#555555;
  }
  *{box-sizing:border-box;margin:0;padding:0}
  html,body{width:924px;height:1200px;overflow:hidden}
  body{background:var(--bg);font-family:"Source Sans 3",sans-serif;color:var(--text);position:relative}
  .spread{position:absolute;left:75px;width:775px;height:502px;background:var(--paper)}
  .spread--outer{top:68px}
  .spread--inner{top:629px}
  .spread-art{position:absolute;inset:0}
  .fold{position:absolute;left:387px;top:0;width:2px;height:100%;background:linear-gradient(90deg,rgba(0,0,0,.06),rgba(0,0,0,0))}
  .abs{position:absolute}

  .brand{display:flex;align-items:center;gap:8px}
  .brand-dot{width:30px;height:30px;border-radius:50%;background:var(--green)}
  .brand-name{font-size:21px;font-weight:600;color:var(--green);letter-spacing:.2px;line-height:1}

  .form-text{left:15px;top:230px;width:350px;font-size:7.2px;line-height:14.5px;color:var(--text)}
  .form-text p{margin-bottom:9px}

  .tagline{right:16px;top:366px;width:260px;text-align:right;font-size:9.4px;line-height:13px;color:var(--text)}
  .phone{display:flex;align-items:center;justify-content:center;gap:5px;width:161px;height:20px;border-radius:10px;background:var(--gold);color:#fff;font-size:13.5px;font-weight:600;letter-spacing:1px}
  .phone svg{width:12px;height:12px}
  .store{right:16px;text-align:right;font-size:6.6px;line-height:10px;color:var(--muted)}

  .intro{left:15px;top:211px;width:355px;font-size:9.4px;line-height:13px;color:var(--text)}
  .benefits{left:17px;top:255px;width:352px;list-style:none}
  .benefits li{position:relative;padding-left:15px;font-size:6.9px;line-height:8.4px;color:var(--muted);margin-bottom:6.4px}
  .benefits li::before{content:"";position:absolute;left:0;top:1px;width:8px;height:6px;background:var(--green);border-radius:0 6px 0 6px}
  .benefits b{font-weight:600;color:var(--green)}

  .details{left:417px;top:30px;width:340px;font-size:7px;line-height:10px;color:var(--muted)}
  .details h3{font-size:7.4px;font-weight:600;color:var(--green);line-height:10px}
  .details p{margin-bottom:8px}
  .details .sub{color:var(--green);font-weight:600}
  .welcome{font-weight:700;color:#111;font-size:7px}
  .address-light{right:16px;font-size:6.6px;color:#fff}
</style>
</head>
<body>

<section class="spread spread--outer">
  <svg class="spread-art" viewBox="0 0 775 502" width="775" height="502">
    <defs>
      <linearGradient id="beach" x1="0" y1="0" x2="1" y2="1">
        <stop offset="0" stop-color="#7aa3a6"/><stop offset=".55" stop-color="#c9bfae"/><stop offset="1" stop-color="#b24a44"/>
      </linearGradient>
      <linearGradient id="garden" x1="0" y1="0" x2="1" y2="1">
        <stop offset="0" stop-color="#6f8f3e"/><stop offset=".5" stop-color="#c9b49a"/><stop offset="1" stop-color="#4f7a2c"/>
      </linearGradient>
    </defs>
    <path role="img" aria-label="Fotografía de la playa del hotel con sombrillas rojas y alberca" d="M0 0H388V100Q250 126 130 110Q55 100 0 112Z" fill="url(#beach)"/>
    <path d="M0 110Q60 100 130 112Q250 128 388 102V110Q250 140 130 122Q60 112 0 122Z" fill="var(--green-light)"/>
    <circle role="img" aria-label="Fotografía de una flor tropical roja" cx="250" cy="92" r="34" fill="#b83a4a" stroke="var(--gold)" stroke-width="2"/>
    <circle role="img" aria-label="Fotografía de un arreglo floral de aves del paraíso" cx="337" cy="92" r="38" fill="#c9a36a" stroke="var(--gold)" stroke-width="2"/>
    <rect role="img" aria-label="Fotografía de huevos de granja sobre tela de yute" x="15" y="410" width="102" height="72" fill="#a6876a" stroke="#c8c8c8"/>
    <rect role="img" aria-label="Fotografía de jabones artesanales y aceite" x="125" y="410" width="102" height="72" fill="#c7ab7c" stroke="#c8c8c8"/>
    <rect role="img" aria-label="Fotografía de un tarro de miel con panal" x="235" y="410" width="102" height="72" fill="#a5641f" stroke="#c8c8c8"/>

    <path role="img" aria-label="Fotografía de una familia plantando flores en el jardín" d="M388 0H775V180Q600 215 470 300Q420 340 395 390L388 400Z" fill="url(#garden)"/>
    <path d="M338 502Q370 380 470 300Q600 215 775 180V206Q620 236 500 312Q412 382 390 502Z" fill="var(--green-light)"/>
    <path d="M390 502Q412 382 500 312Q620 236 775 206V226Q640 256 520 328Q442 392 432 502Z" fill="var(--green)"/>
  </svg>
  <div class="fold"></div>

  <div class="abs brand" style="left:125px;top:150px"><span class="brand-dot"></span><span class="brand-name">verano habitat</span></div>
  <div class="abs form-text">
    <p>Yo ...................................................................................................... , acepto pertenecer al<br>Club VeranoHabitat, por lo cual autorizo un cargo mensual a mi TC por un importe de $ _____ .00<br>que será cargado el día __________________ .</p>
    <p style="margin-top:14px">Estoy de acuerdo que el cargo será recurrente hasta que cancele mi suscripción, dando aviso al<br>correo, con 30 días de anticipación.</p>
    <p style="margin-top:14px">Así mismo, estoy de acuerdo que los días de entrega serán los días ____________,<br>del mes en curso a mi domicilio en ___________.</p>
  </div>

  <div class="abs brand" style="left:602px;top:282px"><span class="brand-dot"></span><span class="brand-name">verano habitat</span></div>
  <p class="abs tagline">VERANO HABITAT comparte una filosofía de vida; la oportunidad de regresar al origen, de conectarse con las raíces y la naturaleza, crear vida en tierra fértil y brindarle este regalo a Usted y a su familia directamente a la puerta de su casa.</p>
  <div class="abs phone" style="left:598px;top:441px">
    <svg viewBox="0 0 24 24"><circle cx="12" cy="12" r="10.5" fill="none" stroke="#fff" stroke-width="2"/><path d="M8.5 6.5l2 2-1 1.6a7 7 0 0 0 4.4 4.4l1.6-1 2 2-1.3 1.6C12 17.5 6.5 12 6.9 7.8Z" fill="#fff"/></svg>
    9984.27.60.15
  </div>
  <p class="abs store" style="top:472px">Nuestra tienda esta ubicada en:<br>AV. LAS PALMAS 48, SMZ. 7, CANCUN, QUINTANA ROO, CP. 77510</p>
</section>

<section class="spread spread--inner">
  <svg class="spread-art" viewBox="0 0 775 502" width="775" height="502">
    <defs>
      <linearGradient id="forest" x1="0" y1="0" x2="1" y2="1">
        <stop offset="0" stop-color="#3f6a24"/><stop offset=".5" stop-color="#9bb37a"/><stop offset="1" stop-color="#587f33"/>
      </linearGradient>
      <radialGradient id="bouquet" cx=".5" cy=".5" r=".5">
        <stop offset="0" stop-color="#9e2b1f"/><stop offset=".7" stop-color="#5b3a20"/><stop offset="1" stop-color="#4c8426" stop-opacity="0"/>
      </radialGradient>
    </defs>
    <path role="img" aria-label="Fotografía de un padre y su hijo cosechando en la selva" d="M0 0H388V8Q200 160 0 172Z" fill="url(#forest)"/>
    <path d="M0 170Q200 158 388 6V30Q220 178 0 186Z" fill="var(--green-light)"/>
    <circle role="img" aria-label="Fotografía de papayas partidas" cx="329" cy="67" r="46" fill="#e0923a" stroke="var(--gold)" stroke-width="2"/>
    <circle role="img" aria-label="Fotografía de una piña en la planta" cx="223" cy="135" r="64" fill="#8a6a3a" stroke="var(--gold)" stroke-width="2"/>

    <path d="M383 502Q445 395 560 345Q660 318 775 322V342Q670 340 570 370Q462 410 402 502Z" fill="var(--green-light)"/>
    <path d="M402 502Q462 410 570 370Q670 340 775 342V502Z" fill="var(--green-dark)"/>
    <ellipse role="img" aria-label="Fotografía de un arreglo floral tropical con heliconias y aves del paraíso" cx="688" cy="335" rx="76" ry="92" fill="url(#bouquet)"/>
  </svg>
  <div class="fold"></div>

  <p class="abs intro">Al formar parte de VeranoHabitat Club, recibirá mensualmente los siguientes artículos directamente a la dirección que Usted nos proporciones y el cargo se hará directamente a su tarjeta de crédito.</p>
  <ul class="abs benefits">
    <li><b>Dos arreglos florales al mes (a escoger entre los modelos (............y ...........)</b> - A diferencia de las flores de tienda o supermercado, nuestras flores son más frescas porque llegan directamente de la granja en la selva donde son cultivadas a unos minutos del centro de Cancún en la localidad de Santa Clara. Cada arreglo contiene entre 10 y 12 flores y la variedad consiste en la cosecha de la fecha de entrega.</li>
    <li><b>Dos jabones orgánicos</b> - Elaborados con sustancias naturales coco, avena, rosas, jengibre, café, neem, romero, o sal que NO apoyan las empresas químicas. Invertir en productos de jabón orgánico es evitar toxinas que son nocivas para su piel y para el ambiente.</li>
    <li><b>Un pomo de miel orgánica de 250 ml. marca Verano</b> - Producida en colmenas localizadas en la granja, libres de pesticidas y envasada sin conservadores.</li>
    <li><b>30 huevos de pastoreo</b> - En la producción de estos huevos, las gallinas tienen un espacio para caminar, extender sus alas y realizar otras importantes conductas naturales. Su alimentación es 100% natural y el resultado son huevos muy saludables.</li>
    <li><b>Un paquete de galletas caseras marca Verano</b> - Deliciosas galletas muy saludables, el aceite de coco, las pasas, la avena, aportan más nutrientes resultando en un producto super nutritivo.</li>
    <li><b>Fruta fresca de temporada</b> - Papaya, pina, pina, melón, limones. De acuerdo a la temporada y la calidad de la cosecha se entregara dentro de su pedido la calidad más selecta.</li>
    <li><b>Dulce de Ate 250 gramos</b> - Dulce elaborado con fruta tales como , manzana, durazno, membrillo, elaborados por productores mexicanos que serán un deleite para su hogar.</li>
  </ul>

  <div class="abs details">
    <h3>Entrega a Domicilio</h3>
    <p>La entrega se puede fijar entre los días 1 y 5 de cada mes sin costo alguno El primer arreglo floral se entregaría en esta fecha y el segundo arreglo entre los días 15 y 20 del mismo mes.</p>
    <h3>BENEFICIOS ADICIONALES</h3>
    <p><span class="sub">• Acceso exclusivo</span><br>Como parte desu afiliación recibirá una tarjeta VeranoHabitat y podrá utilizarla comoacceso y DAY PASS al Hotel Coral Bahía pagando únicamente 50% del costo por persona del Todo Incluido (menores de 6 años GRATIS ) Máximo 4 Adultos.<br>Regalo por Referido................? Al referir a 5 personas para inscribirse a VeranoHabitat Club Usted recibirá ......</p>
    <p><span class="sub">• Reconocimiento de Lealtad</span><br>Para agradecer su compromiso y confianza, como regalo de aniversario al cumplir los 24 meses ininterrumpidos de servicio de entrega, se le otorgara un certificado de estancia de 3 días y 2 noches en plan todo incluido para Dos Adultos en cualquiera de los Hoteles de la cadena BahíaGroup.</p>
    <p style="margin-top:14px">En resumen, con la pequeña inversión que hará cuidando de su salud y de los suyospodrá disfrutar de un escape de la rutina diaria por unos días sin costos adicionales.</p>
    <p class="welcome" style="margin-top:18px">ENHORABUENA, Y BIENVENIDO A LA NUEVA ERA DE VIDA SANA.</p>
  </div>

  <div class="abs phone" style="left:598px;top:435px">
    <svg viewBox="0 0 24 24"><circle cx="12" cy="12" r="10.5" fill="none" stroke="#fff" stroke-width="2"/><path d="M8.5 6.5l2 2-1 1.6a7 7 0 0 0 4.4 4.4l1.6-1 2 2-1.3 1.6C12 17.5 6.5 12 6.9 7.8Z" fill="#fff"/></svg>
    9984 27 60 15
  </div>
  <p class="abs address-light" style="top:468px">AV. LAS PALMAS 48, SMZ. 7, CANCUN, QUINTANA ROO, CP. 77510</p>
</section>

</body>
</html>
```